Business Card & Word Docs from existing Logo

We need a business card with typical information plus layout to include electrical contractors license number, VORLE license and KMT license. We would like a word document layout for a proposal document, opening page with logo and design basic information; proposal to and proposal from and project name and number. Small basic single page letter for general documents. Email signature with logo.

We are an electrical, refrigeration and automation contractor. We work with reducing energy consumption for our customers and complex process solutions in electrical, refrigeration and automation.
Updates

Reason: Final changes/ revisions to designs.

Target Market(s)

Industrial and commercial businesses that require more than your average contractor.

Industry/Entity Type

Electrical

Requirements
Must have
• Propsal document must have a full opening page.

```html
<!DOCTYPE html>
<html lang="en">
<head>
<meta charset="utf-8">
<title>Frostline Contracting – Business Card</title>
<link rel="stylesheet" href="https://fonts.googleapis.com/css2?family=Arimo:wght@400;700&display=swap">
<style>
  :root {
    --page: #ffffff;
    --card: #ffffff;
    --brand-blue: #1a86b8;
    --brand-green: #1f9a4a;
    --ink: #1d1d1d;
    --on-dark: #ffffff;
    --deep-blue: #12527a;
    --teal: #1d6f78;
    --steel: #3d4a60;
  }
  html, body {
    margin: 0;
    width: 1200px;
    height: 900px;
    overflow: hidden;
    background: var(--page);
    font-family: "Arimo", Arial, sans-serif;
  }
  .card {
    position: absolute;
    left: 98px;
    top: 137px;
    width: 1004px;
    height: 626px;
    background: var(--card);
    overflow: hidden;
  }
  .card-backdrop {
    position: absolute;
    inset: 0;
    background:
      radial-gradient(ellipse 560px 520px at 78% 42%, #ffffff 45%, rgba(255,255,255,0) 80%),
      radial-gradient(ellipse 380px 300px at 10% 0%, rgba(40,150,90,0.9), rgba(40,150,90,0) 70%),
      linear-gradient(160deg, var(--teal) 0%, var(--steel) 35%, var(--deep-blue) 65%, #2f86c6 100%);
  }
  .logo-panel {
    position: absolute;
    left: 0;
    top: 44px;
    width: 547px;
    height: 156px;
    background: var(--card);
    border-radius: 0 22px 22px 0;
    box-shadow: 0 0 26px rgba(255,255,255,0.9);
    display: flex;
    align-items: center;
    gap: 22px;
    padding-left: 50px;
    box-sizing: border-box;
  }
  .logo-dot {
    width: 86px;
    height: 86px;
    border-radius: 50%;
    background: var(--brand-green);
    flex: none;
  }
  .logo-name {
    font-weight: 700;
    font-size: 40px;
    line-height: 1.1;
    color: var(--brand-blue);
    letter-spacing: 1px;
  }
  .holder { position: absolute; right: 64px; top: 82px; text-align: right; }
  .holder-name { font-weight: 700; font-size: 40px; color: var(--brand-blue); margin: 0; line-height: 46px; }
  .holder-role { font-size: 30px; color: var(--ink); margin: 0; line-height: 40px; }
  .phones {
    position: absolute;
    right: 695px;
    top: 262px;
    text-align: right;
    color: var(--on-dark);
    font-size: 30px;
    line-height: 40px;
    margin: 0;
  }
  .phones b { font-weight: 700; }
  .details {
    position: absolute;
    right: 52px;
    top: 264px;
    text-align: right;
    font-size: 30px;
    line-height: 40px;
    color: var(--ink);
  }
  .details p { margin: 0; }
  .label { color: var(--brand-blue); font-weight: 700; }
  .gap-label { margin-right: 10px; }
  .licences { margin-top: 49px !important; }
  .address { position: absolute; right: 52px; top: 532px; font-size: 30px; font-weight: 700; color: var(--brand-blue); margin: 0; }
</style>
</head>
<body>
  <section class="card">
    <div class="card-backdrop" role="img" aria-label="Abstract blue, teal and green light streaks fading into white"></div>

    <div class="logo-panel">
      <span class="logo-dot"></span>
      <span class="logo-name">FROSTLINE<br>CONTRACTING</span>
    </div>

    <div class="holder">
      <p class="holder-name">Sam Carter</p>
      <p class="holder-role">Director</p>
    </div>

    <p class="phones">
      <b>T:</b> 07 5550 1234<br>
      <b>F:</b> 07 5550 1234<br>
      <b>M:</b> 0400 555 019
    </p>

    <div class="details">
      <p><span class="label gap-label">E-mail</span> sam@frostline.com.au</p>
      <p><span class="label gap-label">Website</span> www.frostline.com.au</p>
      <p class="licences"><span class="label">Electrical Contractors License</span> 12345</p>
      <p><span class="label">KMT</span> 1234567 &nbsp;|&nbsp; <span class="label">VORLE</span> AA12345</p>
    </div>

    <p class="address">PO Box 4821, Cairns, Queensland, 4870</p>
  </section>
</body>
</html>
```